Letterhead and Business card for Construction company

We need a letterhead and business card with our new company logo. We are based in NY. We develop and build properties.

The design should incorporate some unique feature from the logo (shape, font...). it should look like an extension from it.

Design should be clean and elegant, professional, not too busy.

The letterhead should include:
Logo (attached)
Address
Phone
Email

Please find the attached logo images and AI file.

Target Market(s)

Construction industry professionals

Industry/Entity Type

Construction, Development

Font styles to use
Sans Serif

Colors

Designer to choose colors to be used in the design.

Requirements
Must have
• Design should incorporate logo elements, additional assets are welcome. I'd like to see some other shapes / images invorporated too.

```html
<!DOCTYPE html>
<html lang="en">
<head>
<meta charset="utf-8">
<title>Norvale Contracting – Business Card</title>
<link rel="stylesheet" href="https://fonts.googleapis.com/css2?family=Arimo:wght@400;700&display=swap">
<style>
  :root {
    --bg: #ababab;
    --orange: #f47f20;
    --black: #111111;
    --white: #ffffff;
    --rule: #8a8a8a;
    --text: #1a1a1a;
  }
  * { margin: 0; padding: 0; box-sizing: border-box; }
  html, body { width: 1200px; height: 900px; overflow: hidden; }
  body {
    background: var(--bg);
    font-family: "Arimo", Arial, sans-serif;
    position: relative;
  }
  .card {
    position: absolute;
    left: 285px;
    width: 630px;
    height: 360px;
    overflow: hidden;
    box-shadow: 0 6px 18px rgba(0,0,0,0.25);
  }
  .card-front { top: 50px; background: var(--white); }
  .card-back { top: 480px; background: var(--orange); }

  .front-wave { position: absolute; inset: 0; width: 630px; height: 360px; }

  .brand {
    position: absolute;
    font-weight: 700;
    color: var(--black);
    text-transform: uppercase;
    line-height: 1;
    display: flex;
    align-items: center;
    gap: 12px;
  }
  .brand-mark { width: 22px; height: 22px; background: var(--orange); flex: none; }
  .card-front .brand { left: 36px; top: 78px; font-size: 30px; letter-spacing: 1px; }
  .brand-name span { display: block; }
  .brand-name .sub { font-size: 17px; letter-spacing: 3.5px; margin-top: 6px; }

  .divider {
    position: absolute;
    left: 300px; top: 58px;
    width: 1px; height: 170px;
    background: var(--rule);
  }
  .contact { position: absolute; left: 326px; top: 62px; color: var(--text); }
  .contact-name {
    color: var(--orange);
    font-size: 22px;
    font-weight: 700;
    text-transform: uppercase;
    letter-spacing: 0.5px;
  }
  .contact-role { font-size: 14px; margin-top: 2px; }
  .contact-address { font-size: 15px; line-height: 1.3; margin-top: 14px; }
  .contact-list { list-style: none; margin-top: 12px; font-size: 15px; line-height: 1.45; }
  .contact-list li { display: flex; align-items: center; gap: 8px; }
  .contact-list svg { width: 13px; height: 13px; flex: none; }

  .card-back .brand {
    left: 50%; top: 50%;
    transform: translate(-50%, -50%);
    font-size: 44px;
    letter-spacing: 2px;
    gap: 16px;
  }
  .card-back .brand-mark { width: 30px; height: 30px; background: var(--black); }
  .card-back .brand-name .sub { font-size: 25px; letter-spacing: 5.5px; margin-top: 8px; }
</style>
</head>
<body>
  <section class="card card-front">
    <svg class="front-wave" viewBox="0 0 630 360" aria-hidden="true">
      <path d="M0 128 C110 140 200 290 370 318 C470 334 560 322 630 292 L630 360 L0 360 Z" fill="#f47f20"/>
      <path d="M0 140 C105 150 195 300 372 326 C472 340 560 330 630 304 L630 360 L0 360 Z" fill="#ffffff"/>
      <path d="M0 148 C100 160 190 308 374 332 C474 345 560 338 630 312 L630 360 L0 360 Z" fill="#111111"/>
    </svg>

    <div class="brand">
      <span class="brand-mark"></span>
      <span class="brand-name"><span>Norvale</span><span class="sub">Contracting</span></span>
    </div>

    <div class="divider"></div>

    <div class="contact">
      <p class="contact-name">Daniel Reyes</p>
      <p class="contact-role">Manager</p>
      <p class="contact-address">Your address, city<br>state, ZIP 0000</p>
      <ul class="contact-list">
        <li>
          <svg viewBox="0 0 16 16"><path d="M3 1.5 L6 1.5 L7 5 L5.3 6.3 C6.2 8.2 7.8 9.8 9.7 10.7 L11 9 L14.5 10 L14.5 13 C14.5 14 13.5 14.7 12.5 14.5 C6.8 13.6 2.4 9.2 1.5 3.5 C1.3 2.5 2 1.5 3 1.5 Z" fill="#f47f20"/></svg>
          123-456-2100
        </li>
        <li>
          <svg viewBox="0 0 16 16"><rect x="1.5" y="3.5" width="13" height="9" fill="none" stroke="#f47f20" stroke-width="1.6"/><path d="M1.5 3.5 L8 9 L14.5 3.5" fill="none" stroke="#f47f20" stroke-width="1.6"/></svg>
          youremail@mailbox.com
        </li>
        <li>
          <svg viewBox="0 0 16 16"><circle cx="8" cy="8" r="6.5" fill="none" stroke="#f47f20" stroke-width="1.6"/><path d="M1.5 8 H14.5 M8 1.5 C5 5 5 11 8 14.5 M8 1.5 C11 5 11 11 8 14.5" fill="none" stroke="#f47f20" stroke-width="1.3"/></svg>
          www.yourwebsite.com
        </li>
      </ul>
    </div>
  </section>

  <section class="card card-back">
    <div class="brand">
      <span class="brand-mark"></span>
      <span class="brand-name"><span>Norvale</span><span class="sub">Contracting</span></span>
    </div>
  </section>
</body>
</html>
```